BRIGHT COLORFUL + 55 FAMILY HISTORY BROCHURE 11 x 17 bifold

11 x 17 Bifold Flyer I have given you the Layout I just need you to make it Pretty

YOU DO NOT NEED TO FOLLOW MY LAYOUT, You can but dont have too

Target Market(s)

55 year old consumers, who could choose our service of Hereditary Cancer Screening

Industry/Entity Type

Health And Wellness

Requirements
Must have
• Must be appealing to Grand Parents, must make them want to test , show lots of pictures of grand children, YOU DO NOT NEED TO FOLLOW MY LAYOUT , You can but dont have too
Nice to have
• use our colors of our logo , YOU DO NOT NEED TO FOLLOW MY LAYOUT , You can but dont have too
Should not have
• YOU DO NOT NEED TO FOLLOW MY LAYOUT, You can but dont have too

```html
<!DOCTYPE html>
<html lang="en">
<head>
<meta charset="utf-8">
<title>Family History Brochure Spread</title>
<link href="https://fonts.googleapis.com/css2?family=Open+Sans:ital,wght@0,400;0,600;0,700;1,400&display=swap" rel="stylesheet">
<style>
:root{
  --green-dark:#3f7a2e;
  --green-mid:#5c9a3a;
  --green-light:#9cc25a;
  --navy:#173a7a;
  --navy-deep:#0e2a5e;
  --paper:#f3f4f6;
  --ink:#1e2a3a;
  --white:#ffffff;
  --backdrop:#c9c9c9;
}
*{margin:0;padding:0;box-sizing:border-box}
html,body{width:1200px;height:789px;overflow:hidden;background:var(--backdrop);font-family:"Open Sans",Arial,sans-serif}
.spread{position:relative;width:1200px;height:789px;display:flex}
.page{position:relative;width:600px;height:789px;overflow:hidden}
.page-left{background:var(--paper)}
.page-right{background:var(--paper);box-shadow:inset 12px 0 18px -12px rgba(0,0,0,.25)}
.page-shapes{position:absolute;inset:0;width:600px;height:789px}
.body-copy{position:absolute;font-size:9.6px;line-height:1.42;text-align:justify}
.body-copy p{margin-bottom:7px}
.body-copy b{font-weight:700}
.page-left .body-copy{left:56px;top:46px;width:500px;color:var(--white)}
.headline-left{position:absolute;left:56px;top:348px;width:500px;color:var(--white);font-weight:700;font-size:17px;line-height:1.3}
.headline-left em{display:block;font-weight:600;font-style:normal;font-size:14px;margin-top:6px}
.photo{position:absolute;border-style:solid}
.photo-grandmother{left:96px;top:452px;width:420px;height:216px;border:5px solid var(--white);
  background:linear-gradient(120deg,#f4eee8 0%,#e9d3c2 45%,#c99a7a 75%,#f6f1ec 100%)}
.photo-family{left:70px;top:350px;width:470px;height:262px;border:4px solid var(--navy);
  background:linear-gradient(180deg,#cfe3a8 0%,#8fbf5e 45%,#bcd3e6 70%,#7d94b0 100%)}
.url-band{position:absolute;height:26px;background:var(--navy);color:var(--white);font-size:11px;font-weight:700;display:flex;align-items:center;padding:0 24px}
.page-left .url-band{left:0;top:736px;width:300px}
.page-right .url-band{right:0;top:726px;width:300px;justify-content:flex-end}
.page-right .body-copy{left:48px;top:44px;width:510px;color:var(--ink)}
.headline-right{position:absolute;left:60px;top:628px;width:380px;color:var(--green-dark);font-weight:700;font-size:20px;line-height:1.25}
</style>
</head>
<body>
<div class="spread">
  <section class="page page-left">
    <svg class="page-shapes" viewBox="0 0 600 789" aria-hidden="true">
      <defs>
        <linearGradient id="leftGreen" x1="0" y1="1" x2="1" y2="0">
          <stop offset="0" stop-color="#3a7229"/>
          <stop offset=".6" stop-color="#5c9a3a"/>
          <stop offset="1" stop-color="#a6c85e"/>
        </linearGradient>
      </defs>
      <polygon points="0,0 600,0 600,470 390,789 0,789" fill="url(#leftGreen)"/>
      <polygon points="0,0 70,0 0,96" fill="var(--navy)"/>
      <polygon points="0,728 320,728 320,732 0,732" fill="var(--green-dark)"/>
    </svg>
    <div class="body-copy">
      <p><b>Genetic testing revealed</b> Daniel Whitford carried a mutation that gave him a 55 to 70 percent chance of developing stomach cancer. Early screening revealed there were 14 sites of stage 1A cancer. Once the news sunk in, he realized <b>his Mother Genetic Testing Saved His Life.</b></p>
      <p><b>Genetic Testing Saved My Life.</b> Because of my age and <b>Ashkenazi Jewish ancestry</b>, my doctor recommended Genetic Testing and they were right, I had the BRCA Gene. My older sister was negative. <b>Now we are in control</b>, my younger sister got tested too, and there are steps that can be taken to reduce the risks, including enhanced breast cancer screening, risk-reducing surgeries, and chemoprevention to help prevent or delay the development of cancer.</p>
      <p><b>A breast cancer survivor before age 30:</b> "Genetic testing saved my life!" Megan Lorne was diagnosed with breast cancer two weeks before her 29th birthday. Now 30, she credits her recovery to <b>awareness of a hereditary genetic mutation</b> that predisposed her and her family to the disease. <b>After my mom tested positive for the BRCA 1 gene mutation</b>, I knew genetic testing was something that I would need. <b>Once I tested positive</b>, I was referred to a breast health clinic for <b>increased surveillance</b>. There, my medical care providers were very diligent in making sure I was watched closely. <b>Knowledge is power</b> and, in this case, <b>Genetic testing saved my life!</b></p>
      <p><b>My father had genetic testing</b> and found he had hereditary nonpolyposis colorectal cancer (HNPCC), commonly known as Lynch syndrome. My name is Claire Ashby and I am a 10 year survivor of colorectal cancer. From an early age I learned the importance of screenings and knew about signs and symptoms. <b>Following screening guidelines for individuals at an increased risk &amp; Knowing my family history saved my life!</b></p>
    </div>
    <h2 class="headline-left">A Positive result or finding a mutation is Not a Cancer Diagnosis and does not mean you will ever develop Cancer
      <em>learning if you have an increased risk for cancer can make a difference</em></h2>
    <div class="photo photo-grandmother" role="img" aria-label="Photo of a smiling grandmother and young mother holding a sleeping newborn"></div>
    <div class="url-band">www.kinshipscreening.com</div>
  </section>

  <section class="page page-right">
    <svg class="page-shapes" viewBox="0 0 600 789" aria-hidden="true">
      <defs>
        <linearGradient id="rightGreen" x1="0" y1="1" x2="1" y2="0">
          <stop offset="0" stop-color="#3f7a2e"/>
          <stop offset="1" stop-color="#8dbb52"/>
        </linearGradient>
      </defs>
      <polygon points="0,0 48,0 0,70" fill="var(--green-mid)"/>
      <polygon points="600,480 600,789 400,789" fill="url(#rightGreen)"/>
    </svg>
    <div class="body-copy">
      <p><b>Genetic Testing</b> is done to determine whether family members without obvious illness have inherited the same mutation as a family member who is known to carry a cancer associated mutation. Meaning <b>Will You Help Your Kids &amp; Grand Children</b></p>
      <p><b>What are the benefits of testing?</b> "The Power of Knowledge" <b>Helping Younger Family Members Know if there is a Risk and Preparing for it.</b> Knowing if you have a genetic mutation is that you can work with your doctor to monitor and address your cancer risks. <b>According to the National Wellness Council eating 5 or more Servings of Vegetables &amp; Fruit, and Most Importantly also lowering your intake of red meat, dairy and eggs will help prevent or delay cancer.</b></p>
      <p><b>There are many benefits to getting tested,</b> regardless of the eventual result. If one of your family members - however distant - had cancer, there is a chance that you inherited a gene mutation that not only increases your personal risk of cancer, but also could be passed to the next generation. Those who are carriers of hereditary cancer gene mutations could be at risk of getting cancer earlier in life than the general population. <b>The sooner genetic testing is done, the more likely it is that the risk can be managed appropriately.</b></p>
    </div>
    <div class="photo photo-family" role="img" aria-label="Photo of three generations of a happy family outdoors, grandparents with parents and grandchildren"></div>
    <h2 class="headline-right">There are many Known risk factors for Cancer. GENETICS and FAMILY HISTORY are Often Overlooked.</h2>
    <div class="url-band">www.kinshipscreening.com</div>
  </section>
</div>
</body>
</html>
```